Manufacturer's Representative Group needs a clean new Website

We represent and sell a number of suppliers that design and build products used in Biopharmaceutical manufacturing. Our sales region is in the central US. Our customer base is scientific / engineering based - so clean, we organized design with a focus on the products - easy and clear navigation is necessary. We do not sell direct or warehouse product - so e-commerce is not needed. Our customers will use the website for reference on what we do and offer - we will use the site as a platform to present products from each vendor and the home page will be used to capture an overview and draw users deeper into the site. You can view our current site - which needs A LOT of help to get ideas on products represented and types of products

Target Market(s)

Engineers and Pharmaceutical / Bio pharm end users

Industry/Entity Type

E-Commerce

Number of Pages Required

2 page

Font styles to use
Sans Serif

Requirements
Must have
• I need a home page that provides a snapshot of my company and the product lines we represent - then a second page that I can copy as a template for each line I rep as well as for an "About us / contact" page.
• I would like to be able to manage content on the pages so something easy to adjust pictures or add content is a must
• Must use our logo

```html
<!DOCTYPE html>
<html lang="en">
<head>
<meta charset="utf-8">
<title>Prairie Bio – Home</title>
<link href="https://fonts.googleapis.com/css2?family=Oswald:wght@300;400&display=swap" rel="stylesheet">
<style>
  :root {
    --navy: #26225f;
    --orange: #f0592a;
    --white: #ffffff;
    --grey: #8c8c8c;
    --ink: #1a1a1a;
    --font: "Oswald", sans-serif;
  }
  * { box-sizing: border-box; margin: 0; padding: 0; }
  html, body { width: 1151px; height: 1200px; overflow: hidden; background: var(--white); font-family: var(--font); }
  .page { position: relative; width: 1151px; height: 1200px; }

  .top-rule { position: absolute; left: 0; top: 0; width: 100%; height: 4px; background: var(--orange); }

  .brand { position: absolute; left: 32px; top: 44px; display: flex; align-items: center; gap: 12px; }
  .brand-dot { width: 26px; height: 26px; border-radius: 50%; background: var(--orange); }
  .brand-name { font-size: 40px; font-weight: 400; color: var(--navy); letter-spacing: 0.5px; }

  .search { position: absolute; left: 848px; top: 56px; width: 253px; height: 31px; background: var(--navy); border: 1px solid #111; display: flex; align-items: center; justify-content: space-between; padding: 0 8px; }
  .search-label { color: var(--orange); font-size: 22px; font-weight: 400; line-height: 1; }

  .main-nav { position: absolute; left: 0; top: 129px; width: 100%; height: 33px; background: var(--navy); }
  .main-nav ul { list-style: none; display: flex; position: absolute; right: 60px; top: 0; gap: 50px; }
  .main-nav a { color: var(--white); text-decoration: none; font-size: 26px; font-weight: 300; line-height: 32px; }

  .hero { position: absolute; left: 0; top: 162px; width: 100%; height: 503px;
    background:
      linear-gradient(180deg, rgba(255,255,255,0.55) 0%, rgba(255,255,255,0) 45%),
      linear-gradient(90deg, #5b9bd5 0%, #4a8fd0 10%, #f2c21a 14%, #f7d84a 38%, #ece7d8 46%, #f0efe8 58%, #5b9a3a 62%, #6fae44 80%, #e0452a 88%, #d33a22 100%); }
  .hero-callout { position: absolute; left: 104px; top: 411px; }
  .hero-title { background: var(--navy); color: var(--white); width: 356px; height: 48px; font-size: 29px; font-weight: 400; line-height: 46px; text-align: center; letter-spacing: -0.5px; }
  .hero-sub { margin-left: 32px; margin-top: 2px; background: var(--orange); color: var(--white); width: 274px; height: 83px; font-size: 27px; font-weight: 300; line-height: 32px; text-align: center; padding-top: 10px; }

  .features { position: absolute; left: 0; top: 665px; width: 100%; height: 363px; background: var(--navy); }
  .feature { position: absolute; top: 24px; width: 297px; height: 316px; border: 4px solid var(--white); text-align: center; color: var(--white); }
  .feature svg { display: block; margin: 8px auto 0; }
  .feature p { font-size: 27px; font-weight: 300; line-height: 32px; margin-top: 24px; }
  .feature-1 { left: 58px; } .feature-2 { left: 431px; } .feature-3 { left: 803px; }

  .partners { position: absolute; left: 0; top: 1028px; width: 100%; height: 120px; display: flex; align-items: center; justify-content: space-around; padding: 0 14px; }
  .partner { display: flex; align-items: center; gap: 8px; font-size: 34px; font-weight: 300; color: var(--grey); }
  .partner-mark { width: 22px; height: 22px; border-radius: 50%; background: #6da7d8; }

  .bottom-rule { position: absolute; left: 0; top: 1148px; width: 100%; height: 7px; background: var(--orange); }
  .legal { position: absolute; right: 16px; top: 1162px; font-size: 27px; font-weight: 300; color: var(--ink); }
</style>
</head>
<body>
<div class="page">
  <div class="top-rule"></div>

  <header>
    <div class="brand"><span class="brand-dot"></span><span class="brand-name">Prairie Bio</span></div>
    <div class="search">
      <span class="search-label">search...</span>
      <svg width="22" height="22" viewBox="0 0 22 22" fill="none" stroke="#f0592a" stroke-width="2"><circle cx="9" cy="9" r="7"/><line x1="14" y1="14" x2="20" y2="20"/></svg>
    </div>
  </header>

  <nav class="main-nav">
    <ul>
      <li><a href="#">Home</a></li>
      <li><a href="#">Products</a></li>
      <li><a href="#">Contact</a></li>
    </ul>
  </nav>

  <section class="hero" role="img" aria-label="Close-up photo of laboratory glassware filled with blue, yellow, green and red liquids"></section>
  <div class="hero-callout">
    <h1 class="hero-title">THE BEST QUALITY OUT THERE</h1>
    <p class="hero-sub">We work with only the<br>top brands in the industry.</p>
  </div>

  <section class="features">
    <div class="feature feature-1">
      <svg width="90" height="104" viewBox="0 0 90 104"><path d="M32 6h26M36 6v30L8 90a8 8 0 0 0 7 10h60a8 8 0 0 0 7-10L54 36V6" fill="none" stroke="#f0592a" stroke-width="6" stroke-linejoin="round"/><path d="M22 64h46l12 26a5 5 0 0 1-5 7H15a5 5 0 0 1-5-7z" fill="#f0592a"/></svg>
      <p>Text about your brand<br>and what it is doing that<br>stands out against the<br>rest of the competition.</p>
    </div>
    <div class="feature feature-2">
      <svg width="90" height="104" viewBox="0 0 90 104"><path d="M32 6h26M36 6v30L8 90a8 8 0 0 0 7 10h60a8 8 0 0 0 7-10L54 36V6" fill="none" stroke="#f0592a" stroke-width="6" stroke-linejoin="round"/><path d="M22 64h46l12 26a5 5 0 0 1-5 7H15a5 5 0 0 1-5-7z" fill="#f0592a"/></svg>
      <p>Text about your brand<br>and what it is doing that<br>stands out against the<br>rest of the competition.</p>
    </div>
    <div class="feature feature-3">
      <svg width="90" height="104" viewBox="0 0 90 104"><path d="M32 6h26M36 6v30L8 90a8 8 0 0 0 7 10h60a8 8 0 0 0 7-10L54 36V6" fill="none" stroke="#f0592a" stroke-width="6" stroke-linejoin="round"/><path d="M22 64h46l12 26a5 5 0 0 1-5 7H15a5 5 0 0 1-5-7z" fill="#f0592a"/></svg>
      <p>Text about your brand<br>and what it is doing that<br>stands out against the<br>rest of the competition.</p>
    </div>
  </section>

  <section class="partners" aria-label="Partner brands">
    <div class="partner"><span class="partner-mark"></span>CleanSeal</div>
    <div class="partner">Harlow Pumps</div>
    <div class="partner">Norvane Plastics</div>
    <div class="partner">Veriform</div>
    <div class="partner">Modulon</div>
  </section>

  <div class="bottom-rule"></div>
  <footer class="legal">© Prairie Biosystems, Corp.</footer>
</div>
</body>
</html>
```